We need a fresh, new church business card!!

We need a church business card with basic info to hand out as invites. We are looking for something clean that communicates our basic information clearly.

We are open to square or rectangle card sizes.

General Public

Religious

The attached logo is the only one that I have available. We'd like to see options with with text of the logo lighter and on a dark background as well as options with white/light backgrounds.

Also, we'd like to see option with rounded corners.

• Address - 2718 Maple Row, Rockford, IL 61142
• Website - brookvane.example
• Phone - 815-555-0163
• Service times -
• Sunday - 10am Sunday School
• - 11am Family Worship
• - 6pm Night of Prayer
• Wednesday - 7:30pm Adult Bible Study
• Classes for all ages

```html
<!DOCTYPE html>
<html lang="en">
<head>
<meta charset="utf-8">
<title>Brookvane Pentecostal Church – Business Cards</title>
<link href="https://fonts.googleapis.com/css2?family=Roboto+Slab:wght@300;400;600&display=swap" rel="stylesheet">
<style>
  :root {
    --backdrop: #b0aeaf;
    --card-dark: #3b3836;
    --card-light: #fbfbfa;
    --teal: #5b95a6;
    --swoosh: #7b7b7b;
    --text-grey: #7a7a7a;
    --white: #ffffff;
  }
  html, body {
    margin: 0;
    width: 1200px;
    height: 1200px;
    overflow: hidden;
    background: var(--backdrop);
    font-family: "Roboto Slab", Georgia, serif;
  }
  .card {
    position: absolute;
    width: 712px;
    height: 418px;
    border-radius: 28px;
    overflow: hidden;
  }
  .card-front { left: 238px; top: 118px; background: var(--card-dark); }
  .card-back  { left: 230px; top: 644px; background: var(--card-light); }

  .brand { position: absolute; display: flex; align-items: center; }
  .brand-mark { border-radius: 50%; background: var(--teal); flex: none; }
  .brand-name { font-weight: 300; line-height: 1; }
  .brand-name .line1 { display: block; }
  .brand-name .line2 { display: block; }

  .card-front .brand { left: 120px; top: 164px; }
  .card-front .brand-mark { width: 80px; height: 80px; margin-right: 28px; }
  .card-front .brand-name { color: var(--white); }
  .card-front .line1 { font-size: 50px; letter-spacing: 2px; }
  .card-front .line2 { font-size: 17px; letter-spacing: 4.6px; margin-top: 12px; margin-left: 4px; }

  .card-back .brand { left: 395px; top: 310px; }
  .card-back .brand-mark { width: 46px; height: 46px; margin-right: 16px; }
  .card-back .brand-name { color: var(--text-grey); }
  .card-back .line1 { font-size: 29px; letter-spacing: 1px; }
  .card-back .line2 { font-size: 10px; letter-spacing: 3.2px; margin-top: 6px; margin-left: 2px; }

  .wave { position: absolute; left: 0; top: 0; }

  .contact {
    position: absolute; right: 26px; top: 38px;
    margin: 0; padding: 0; list-style: none;
    color: var(--white); font-size: 17px; font-weight: 300;
    text-align: right; line-height: 26.5px;
  }
  .contact li { display: flex; justify-content: flex-end; align-items: center; gap: 10px; }
  .contact svg { width: 16px; height: 16px; fill: var(--white); }

  .services { position: absolute; left: 45px; top: 126px; color: var(--text-grey); }
  .services-title {
    display: inline-block; border: 2px solid var(--teal);
    padding: 1px 16px; font-size: 19px; font-weight: 400;
    letter-spacing: 0.5px; margin-bottom: 14px;
  }
  .day { color: var(--teal); font-weight: 600; font-size: 18px; margin: 0; line-height: 26px; letter-spacing: 0.5px; }
  .times { margin: 0; padding: 0; list-style: none; font-size: 17.5px; font-weight: 300; line-height: 26.5px; }
  .classes { color: var(--teal); font-weight: 600; font-size: 18px; margin: 18px 0 0 -2px; letter-spacing: 0.5px; }
</style>
</head>
<body>

<section class="card card-front" aria-label="Card front">
  <div class="brand">
    <span class="brand-mark"></span>
    <div class="brand-name">
      <span class="line1">BROOKVANE</span>
      <span class="line2">PENTECOSTAL CHURCH</span>
    </div>
  </div>
</section>

<section class="card card-back" aria-label="Card back">
  <svg class="wave" width="712" height="418" viewBox="0 0 712 418" aria-hidden="true">
    <path fill="var(--teal)" d="M0,0 H712 V196 C600,192 520,40 260,38 C150,38 60,52 0,62 Z"/>
    <path fill="var(--swoosh)" d="M0,68 C70,50 160,40 260,42 C500,46 560,200 712,204 V220 C560,216 480,64 280,60 C170,58 80,74 0,92 Z"/>
    <path fill="var(--swoosh)" d="M90,78 C160,64 240,60 320,64 C470,74 560,200 712,214 V222 C560,212 470,84 320,74 C240,70 170,72 90,78 Z"/>
  </svg>

  <ul class="contact">
    <li>2718 Maple Row, Rockford, IL 61142
      <svg viewBox="0 0 16 16" aria-hidden="true"><path d="M2 6c0-2 2-3 6-3s6 1 6 3v1h-3V5.5H5V7H2z M4 8h8l2 5H2z"/></svg></li>
    <li>www.brookvane.example
      <svg viewBox="0 0 16 16" aria-hidden="true"><path d="M1 3h14v10H1z" fill="none" stroke="#fff" stroke-width="1.6"/><path d="M1 3l7 6 7-6" fill="none" stroke="#fff" stroke-width="1.6"/></svg></li>
    <li>815-555-0163
      <svg viewBox="0 0 16 16" aria-hidden="true"><path d="M8 1a5 5 0 0 1 5 5c0 4-5 9-5 9S3 10 3 6a5 5 0 0 1 5-5zm0 3a2 2 0 1 0 0 4 2 2 0 0 0 0-4z"/></svg></li>
  </ul>

  <div class="services">
    <div class="services-title">SERVICE TIMES</div>
    <p class="day">SUNDAY</p>
    <ul class="times">
      <li>Sunday School ..... 10:00am</li>
      <li>Family Worship .... 11:00am</li>
      <li>Night of Prayer ...... 6:00pm</li>
    </ul>
    <p class="day">WEDNESDAY</p>
    <ul class="times">
      <li>Adult Bible Study ... 7:30pm</li>
    </ul>
    <p class="classes">CLASSES FOR ALL AGES</p>
  </div>

  <div class="brand">
    <span class="brand-mark"></span>
    <div class="brand-name">
      <span class="line1">BROOKVANE</span>
      <span class="line2">PENTECOSTAL CHURCH</span>
    </div>
  </div>
</section>

</body>
</html>
```